Family Office for small businesses needs clear web site

I founded VORUSK Family Office, which is a french family office design to change the relationship between the customer and the wealth manager/insurance broker.
The main focus is : we give back to the client all the commissions / hidden costs we gain from the insurance companies / real estate builders and we bill to the client an annual fee proportional to the wealth. Thus a transparent relationship exempt from conflict of interest

I want a WORPRESS theme design that will be easily customizable in the future. Using and existing wordpress theme is not a problem, as long as i get to customize it in the future if necessary.
I want the web site to be Simple, clear, explaining the concepts detailed in the word doc i join to this project
In the chart are some of the things we do (not all, but most).
Also i joined some question a client might ask himself before calling us

i am available to clarify any issue or concepts

Reason: I want to let new designer submit their proposal. I really wish to conclude this design contest to move forward on other projects.

Target Market(s)

small businesses, specically their boss

Industry/Entity Type

Office

Number of Pages Required

1 page

Font styles to use
Serif

Colors
85acd3
3176b5
0455a3
cedeed
eaf1f7
cee9f5
85cae6
33a6d7
0692cd

Requirements
Must have
• I would like to have a one page wordpress theme personalized by a designer.
• I don't really care if you use an existing wordpress theme, as long as it can be upgraded/customized later on using wordpress/admin.
• I can even provide some themes I bought if it can help maintain the budget..
• O I can pay additional fee for a theme you bought to provide the design..

```html
<!DOCTYPE html>
<html lang="en">
<head>
<meta charset="utf-8">
<title>VORUSK Family Office</title>
<link href="https://fonts.googleapis.com/css2?family=Lato:ital,wght@0,300;0,400;0,700;1,400&family=PT+Serif:ital,wght@0,400;0,700;1,400;1,700&display=swap" rel="stylesheet">
<style>
:root{
  --blue-light:#85acd3;
  --blue-mid:#3176b5;
  --blue-deep:#0455a3;
  --blue-pale:#cedeed;
  --blue-mist:#eaf1f7;
  --ink:#2b2b2b;
  --grey-text:#666;
  --grey-line:#dcdcdc;
  --grey-panel:#efefef;
  --dark:#3b3b3b;
  --darker:#2a2a2a;
  --white:#fff;
}
*{box-sizing:border-box;margin:0;padding:0}
html,body{width:1200px;height:4400px;overflow:hidden}
body{font-family:"PT Serif",Georgia,serif;color:var(--ink);background:var(--white);position:relative}
section,header,footer{position:absolute;left:0;width:1200px}

/* header */
.site-header{top:0;height:60px;background:var(--white);border-bottom:1px solid var(--grey-line)}
.brand{position:absolute;left:40px;top:12px;display:flex;align-items:center;gap:10px}
.brand-square{width:34px;height:34px;background:var(--blue-deep)}
.brand-name{font-family:"Lato",sans-serif;font-weight:700;font-size:18px;color:var(--blue-deep);letter-spacing:1px;white-space:nowrap}
.top-info{position:absolute;top:8px;left:300px;right:40px;display:flex;gap:40px;font-family:"Lato",sans-serif;font-size:11px;color:var(--grey-text);white-space:nowrap}
.top-info .req{margin-left:auto;color:var(--blue-deep)}
.main-nav{position:absolute;right:40px;top:32px;display:flex;gap:38px;font-family:"Lato",sans-serif;font-size:13px;color:var(--grey-text)}

/* hero */
.hero{top:60px;height:520px}
.hero-photo{position:absolute;inset:0;background:linear-gradient(180deg,#5a5a5a 0%,#8a8a8a 35%,#6f6f6f 70%,#b9b9b9 100%)}
.hero-copy{position:absolute;left:110px;top:40px;width:520px;color:var(--white)}
.hero-copy h1{font-family:"Lato",sans-serif;font-weight:300;font-size:44px;line-height:1.1}
.hero-copy p{margin-top:18px;font-size:15px;line-height:1.45}
.service-cards{top:500px;left:110px;width:980px;height:140px;display:flex;gap:20px}
.service-card{flex:1;background:var(--white);box-shadow:0 2px 8px rgba(0,0,0,.15);text-align:center;padding-top:18px}
.service-card h3{font-family:"PT Serif",serif;font-style:italic;font-weight:700;font-size:16px;color:var(--blue-deep);margin-top:8px}
.service-card p{font-family:"Lato",sans-serif;font-size:11px;color:var(--grey-text);margin-top:6px;line-height:1.4}

/* about */
.about{top:700px;height:600px}
.about-text{position:absolute;left:110px;top:20px;width:640px}
.about-text h2{font-weight:700;font-size:25px;line-height:1.3}
.about-text h2 em{font-weight:400}
.about-text p{font-family:"Lato",sans-serif;font-size:12.5px;color:var(--grey-text);line-height:1.55;margin-top:12px}
.about-text h4{font-size:20px;font-weight:700;margin-top:20px}
.about-text h5{font-family:"Lato",sans-serif;font-size:11.5px;font-weight:400;color:var(--blue-mid);margin-top:10px}
.about-text h5+p{margin-top:2px}
.more-link{display:block;font-family:"Lato",sans-serif;font-size:11px;font-weight:700;color:var(--blue-mid);letter-spacing:1px;margin-top:22px}
.portrait{position:absolute;left:790px;top:130px;width:300px;height:290px;background:linear-gradient(160deg,#4a4a4a,#222)}
.quote-box{position:absolute;left:790px;top:420px;width:300px;height:180px;background:var(--blue-mist);padding:18px 22px}
.quote-box blockquote{font-size:18px;font-style:italic;line-height:1.3}
.quote-box cite{display:block;font-family:"Lato",sans-serif;font-style:normal;font-size:11px;color:var(--grey-text);margin-top:12px;border-top:1px solid var(--grey-line);padding-top:8px}

/* services band */
.services{top:1360px;height:440px;background:var(--blue-mid);color:var(--white);text-align:center}
.services h2{font-family:"Lato",sans-serif;font-weight:300;font-size:40px;margin-top:40px}
.services .lead{width:760px;margin:16px auto 0;font-size:13.5px;line-height:1.5}
.benefit-cards{position:absolute;left:110px;top:190px;width:980px;display:flex;gap:40px}
.benefit{flex:1;height:180px;background:var(--blue-deep);padding-top:22px}
.benefit h3{font-style:italic;font-weight:400;font-size:18px;margin-top:10px}
.benefit p{font-family:"Lato",sans-serif;font-size:11.5px;line-height:1.4;margin:6px 30px 0}

/* process */
.process{top:1860px;height:940px}
.process-panel{position:absolute;left:100px;top:0;width:300px;height:940px;background:var(--grey-panel);padding:30px 28px}
.process-panel h2{font-family:"Lato",sans-serif;font-weight:300;font-size:36px;line-height:1.15}
.process-panel .intro{font-family:"Lato",sans-serif;font-size:11.5px;color:var(--grey-text);line-height:1.5;margin-top:14px}
.step{display:flex;gap:12px;margin-top:24px}
.step-num{flex:0 0 30px;height:30px;border-radius:50%;background:var(--blue-deep);color:var(--white);font-family:"Lato",sans-serif;font-size:15px;display:flex;align-items:center;justify-content:center}
.step h3{font-family:"Lato",sans-serif;font-weight:400;font-size:21px;color:var(--ink)}
.step p{font-family:"Lato",sans-serif;font-size:11.5px;color:var(--grey-text);line-height:1.45;margin-top:6px}
.team-photo{position:absolute;left:430px;top:40px;width:670px;height:400px;background:linear-gradient(135deg,#e8d8c4,#c9b59c 50%,#a3b7cc)}
.faq{position:absolute;left:430px;top:470px;width:590px;list-style:none}
.faq li{display:flex;justify-content:space-between;height:40px;align-items:center;border-bottom:1px solid var(--grey-line);font-size:14px;padding:0 8px}
.faq li span{color:var(--grey-text);font-family:"Lato",sans-serif}
.faq-more{position:absolute;left:438px;top:810px;font-family:"Lato",sans-serif;font-size:11px;font-weight:700;color:var(--blue-mid);letter-spacing:1px}

/* testimonials */
.testimonials{top:2840px;height:500px;background:var(--blue-mist)}
.testimonials h2{font-family:"Lato",sans-serif;font-weight:300;font-size:38px;text-align:center;margin-top:50px}
.client-photo{position:absolute;left:300px;top:150px;width:230px;height:240px;background:linear-gradient(160deg,#9aa8b6,#3d4a58)}
.testimonial{position:absolute;left:640px;top:160px;width:300px;padding-left:28px;border-left:1px solid var(--grey-line)}
.testimonial blockquote{font-style:italic;font-size:23px;line-height:1.25;color:#444}
.testimonial cite{display:block;font-family:"Lato",sans-serif;font-style:normal;font-size:12px;color:var(--grey-text);margin-top:14px}

/* consultation */
.consultation{top:3340px;height:500px;background:var(--dark);color:var(--white);text-align:center}
.consultation h2{font-family:"Lato",sans-serif;font-weight:300;font-size:38px;margin-top:70px}
.consultation .lead{width:640px;margin:10px auto 0;font-size:12.5px;line-height:1.45}
.form{position:absolute;left:220px;top:200px;width:760px}
.form-row{display:flex;gap:10px}
.field{flex:1;height:34px;border:1px solid #666;background:#4a4a4a;font-family:"Lato",sans-serif;font-size:12px;color:#ddd;text-align:left;padding:9px 12px}
.field.select{background:#262626;display:flex;justify-content:space-between}
.field.area{height:110px;margin-top:10px}
.send{display:inline-block;margin-top:20px;border:1px solid #999;padding:10px 26px;font-family:"Lato",sans-serif;font-size:11px;letter-spacing:1.5px;font-weight:700}

/* footer */
.site-footer{top:3840px;height:560px;background:var(--darker);color:#ddd;font-family:"Lato",sans-serif}
.back-top{position:absolute;left:560px;top:30px;width:80px;text-align:center;font-size:10px;letter-spacing:1.5px}
.footer-nav{position:absolute;left:110px;top:170px;list-style:none;font-size:15px;line-height:1.75}
.footer-col{position:absolute;top:170px;font-size:14px;line-height:1.9}
.footer-col .row{display:flex;gap:12px;align-items:center;white-space:nowrap}
.footer-col small{display:block;font-size:10px;letter-spacing:1px;color:#999;margin:2px 0 10px 24px}
.footer-brand{position:absolute;left:500px;top:420px;display:flex;align-items:center;gap:10px}
.footer-brand .brand-square{background:var(--white)}
.footer-brand .brand-name{color:var(--white)}
.copyright{position:absolute;left:0;width:1200px;top:500px;text-align:center;font-size:10px;color:#999}
</style>
</head>
<body>

<header class="site-header">
  <div class="brand"><div class="brand-square"></div><span class="brand-name">VORUSK Family Office</span></div>
  <div class="top-info">
    <span>&#9743; +33 1 45 90 30 10</span>
    <span>&#9679; 7, rue Lemaire 75002 Paris</span>
    <span class="req">&#9993; Request a consultation</span>
  </div>
  <nav class="main-nav"><span>Home</span><span>About us</span><span>Practice Areas</span><span>Q&amp;A</span><span>Contact</span></nav>
</header>

<section class="hero">
  <div class="hero-photo" role="img" aria-label="Black and white photograph of advisors in a business meeting"></div>
  <div class="hero-copy">
    <h1>Reliable and effective<br>wealth management</h1>
    <p>We offer a broad range of wealth planning services and advice, and we provide you with in-depth guidance to help you preserve your wealth and transmit it calmly between generations.</p>
  </div>
</section>

<section class="service-cards">
  <div class="service-card">
    <svg width="36" height="36" viewBox="0 0 36 36"><rect x="6" y="18" width="5" height="12" fill="#0455a3"/><rect x="15" y="12" width="5" height="18" fill="#0455a3"/><rect x="24" y="6" width="5" height="24" fill="#0455a3"/></svg>
    <h3>Strategic consulting</h3>
    <p>Clear guidance for your<br>key financial choices.</p>
  </div>
  <div class="service-card">
    <svg width="36" height="36" viewBox="0 0 36 36"><circle cx="18" cy="18" r="11" fill="none" stroke="#0455a3" stroke-width="3"/><path d="M12 18l4 4 8-8" fill="none" stroke="#0455a3" stroke-width="3"/></svg>
    <h3>Operational Advice</h3>
    <p>Hands-on support for<br>each step you take.</p>
  </div>
  <div class="service-card">
    <svg width="36" height="36" viewBox="0 0 36 36"><path d="M4 18L18 6l14 12" fill="none" stroke="#0455a3" stroke-width="3"/><rect x="10" y="17" width="16" height="13" fill="#0455a3"/></svg>
    <h3>Family counseling</h3>
    <p>Advice that protects<br>every generation.</p>
  </div>
</section>

<section class="about">
  <div class="about-text">
    <h2>We are a family office based in <em>Paris</em>. Our ambition is to become the trusted men of families and institutional. We only act in your <em>interest</em>.</h2>
    <p>We assist our clients to decide, ensure the operational implementation of their decisions and to monitor them over time and be a real organizing power. We have our own beliefs and we defend them.</p>
    <p>In order to accompany the lives of our people and their families, we are available to surround and accompany them over one or more generations. We place humans at the heart of our conception of the family office business.</p>
    <h4>Vorusk is&hellip;</h4>
    <h5>Independent</h5>
    <p>Vorusk is an independent company, fully owned by its partners. We do not depend on any financial organization, allowing us to deliver our services with the utmost objectivity.</p>
    <h5>Unbiased, honest and get returned</h5>
    <p>We do not distribute any financial product and all commissions that we would be led to perceive are reassigned. Our services are unbiased and fees are exclusively paid by our customers.</p>
    <h5>Up-to-date</h5>
    <p>We continuously invest in technology and human resources to improve productivity and quality. We formalized the client-retirement processes, written procedures and ethical rules.</p>
    <span class="more-link">&rsaquo; EXPLORE MORE ABOUT VORUSK</span>
  </div>
  <div class="portrait" role="img" aria-label="Portrait of the founder in a dark suit"></div>
  <div class="quote-box">
    <blockquote>&ldquo;We work to help you retain the competitive advantage and disrupt the traditional wealth management industry as we know it.&rdquo;</blockquote>
    <cite>Dr. Henri Valmont &ndash; CEO</cite>
  </div>
</section>

<section class="services">
  <h2>What we can do for you.</h2>
  <p class="lead">We are specialized and focused in what we do well: advanced planning, investment consulting and relationship management. We have a range of expertise here so you have everything at hand, depending on your personal situation and the plan that we agree on together.</p>
  <div class="benefit-cards">
    <div class="benefit">
      <svg width="40" height="40" viewBox="0 0 40 40"><path d="M6 30l10-10 7 6 11-14" fill="none" stroke="#fff" stroke-width="3"/><path d="M28 12h6v6" fill="none" stroke="#fff" stroke-width="3"/></svg>
      <h3>Boost your incomes</h3>
      <p>We are working to earn money for our customers and make them wealthier.</p>
    </div>
    <div class="benefit">
      <svg width="40" height="40" viewBox="0 0 40 40"><circle cx="13" cy="14" r="5" fill="#fff"/><circle cx="27" cy="14" r="5" fill="#fff"/><path d="M4 32c0-7 4-11 9-11s9 4 9 11M18 32c0-7 4-11 9-11s9 4 9 11" fill="#fff"/></svg>
      <h3>Efficient collaboration</h3>
      <p>Our clients judge us on our efficiency above all, our ability to sustain their wealth over time.</p>
    </div>
    <div class="benefit">
      <svg width="40" height="40" viewBox="0 0 40 40"><circle cx="20" cy="20" r="14" fill="none" stroke="#fff" stroke-width="3"/><path d="M13 20l5 5 9-10" fill="none" stroke="#fff" stroke-width="3"/></svg>
      <h3>Simple process</h3>
      <p>We are available to surround and accompany our clients on one or more generations.</p>
    </div>
  </div>
</section>

<section class="process">
  <div class="process-panel">
    <h2>Vorusk&rsquo;s proven process</h2>
    <p class="intro">Our process is the result of significant field research which, having been put into practice, exhibits a proven track record of success so you can get results without wasting your time and money.</p>
    <div class="step"><div class="step-num">1</div><div><h3>Discovery meeting</h3><p>Request a consultation. We will arrange meeting so we can discuss values, goals and current financials in order to establish wisest recommendations.</p></div></div>
    <div class="step"><div class="step-num">2</div><div><h3>Determine a plan</h3><p>Based on our analysis, we will prepare you a comprehensive solution that understands the best your situation, objectives and recommendations.</p></div></div>
    <div class="step"><div class="step-num">3</div><div><h3>Make a commitment</h3><p>Both parties understand their responsibilities and we value in entering a relationship. A commitment meeting will take place.</p></div></div>
    <div class="step"><div class="step-num">4</div><div><h3>Follow-up</h3><p>We work in tandem with your advisor. Our key role is to realize the wellbeing of all stakeholders; we also ensure coordination.</p></div></div>
  </div>
  <div class="team-photo" role="img" aria-label="Photograph of a smiling team working together in a bright office"></div>
  <ul class="faq">
    <li>I want to prepare my transmission/heritage<span>+</span></li>
    <li>I want to save for retirement<span>+</span></li>
    <li>I want to cover rights of succession<span>+</span></li>
    <li>I want to prepare my business transition<span>+</span></li>
    <li>I want to invest in real estate, what to choose ?<span>+</span></li>
    <li>I have plenty contract savings, how optimize?<span>+</span></li>
    <li>I want to save for retire<span>+</span></li>
    <li>I want to cover rights succession<span>+</span></li>
  </ul>
  <span class="faq-more">&rsaquo; EXPLORE ALL ANSWERS</span>
</section>

<section class="testimonials">
  <h2>Testimonials</h2>
  <div class="client-photo" role="img" aria-label="Portrait of a client in a blue suit"></div>
  <div class="testimonial">
    <blockquote>&ldquo;It&rsquo;s not just about business. Business and friendships do not often go together, but now we need that trust. However, they must be fully transparent and irreproachable.&rdquo;</blockquote>
    <cite>Marc Delorme &ndash; Big Data Engineer</cite>
  </div>
</section>

<section class="consultation">
  <h2>Request a consultation.</h2>
  <p class="lead">Please fill out the form below to receive a initial consultation&rsquo;s meeting arrangement. Required information are confidential and used only for consultation request. We sincerely respect your privacy.</p>
  <div class="form">
    <div class="form-row">
      <div class="field">Full Name</div>
      <div class="field">Phone number</div>
      <div class="field select"><span>Real Estate Investments</span><span>&#9662;</span></div>
    </div>
    <div class="field area">Description</div>
    <span class="send">SEND YOUR REQUEST</span>
  </div>
</section>

<footer class="site-footer">
  <div class="back-top">
    <svg width="30" height="40" viewBox="0 0 30 40"><path d="M15 38V4M5 14L15 4l10 10" fill="none" stroke="#ddd" stroke-width="2"/></svg>
    <div>BACK TO TOP</div>
  </div>
  <ul class="footer-nav"><li>Home</li><li>About us</li><li>Practice Areas</li><li>Q&amp;A</li><li>Contact</li></ul>
  <div class="footer-col" style="left:440px">
    <div class="row"><span>&#9743;</span>+33 1 45 90 30 10</div>
    <div class="row"><span>&#9743;</span>+33 5 40 12 88 60</div>
    <div class="row" style="margin-top:22px"><span>&#9993;</span>contact@vorusk.fr</div>
  </div>
  <div class="footer-col" style="left:760px">
    <div class="row"><span>&#9679;</span>12, rue des Tamaris - 64200 Biarritz</div>
    <small>GET DIRECTIONS ON THE MAP</small>
    <div class="row"><span>&#9679;</span>7, rue Lemaire - 75002 Paris</div>
    <small>GET DIRECTIONS ON THE MAP</small>
  </div>
  <div class="footer-brand"><div class="brand-square"></div><span class="brand-name">VORUSK Family Office</span></div>
  <div class="copyright">&copy; 2016 Vorusk SARL. All rights reserved.</div>
</footer>

</body>
</html>
```